Blue Heron IT Business Card - Clean, Simple

Need a simple, clean standard sized business card for an IT consulting business using existing logo and company colours. Background should be mainly white. Feel free to be creative but clean, simple, quiet design is preferred. Font is specified in logo but any sans serif fonts work.

Contact Information for card is as follows (doesn't need to be in this exact order):

Martin Calloway
Owner
martin@blueheronit.ca
705-391-2586
www.blueheronit.ca

Target Market(s)

Small to medium sized business.

Industry/Entity Type

IT Consulting

Contact Information for Business Card

Logo and contact info.

Font styles to use
Sans Serif

Colors
EE7325
F08F49
F5BC92
FAE3D3
FDF4ED

Requirements
Must have
• All white or mostly white background.

```html
<!DOCTYPE html>
<html lang="en">
<head>
<meta charset="utf-8">
<title>Blue Heron IT – Business Card</title>
<link rel="stylesheet" href="https://fonts.googleapis.com/css2?family=Montserrat:wght@400;500;600&display=swap">
<style>
  :root {
    --canvas-bg: #ebebeb;
    --card-bg: #ffffff;
    --ink: #2d2d2d;
    --ink-soft: #3a3a3a;
    --brand: #ee7325;
    --brand-light: #f08f49;
    --brand-pale: #f5bc92;
  }
  * { margin: 0; padding: 0; box-sizing: border-box; }
  html, body {
    width: 1200px;
    height: 1000px;
    overflow: hidden;
    background: var(--canvas-bg);
    font-family: "Montserrat", sans-serif;
    color: var(--ink);
  }
  .stage { position: relative; width: 1200px; height: 1000px; }
  .card {
    position: absolute;
    left: 316px;
    width: 568px;
    height: 347px;
    background: var(--card-bg);
  }
  .card--front { top: 133px; }
  .card--back { top: 521px; width: 567px; }

  .brand-mark {
    position: absolute;
    left: 50%;
    top: 118px;
    width: 56px;
    height: 56px;
    margin-left: -28px;
    border-radius: 50%;
    background: var(--brand);
  }
  .brand-name {
    position: absolute;
    left: 0;
    right: 0;
    top: 205px;
    text-align: center;
    font-size: 44px;
    font-weight: 500;
    letter-spacing: -0.5px;
    line-height: 1;
    color: var(--ink);
  }

  .holder { position: absolute; left: 50px; top: 100px; }
  .holder__name { font-size: 18px; font-weight: 600; color: var(--ink); line-height: 1.2; }
  .holder__role { margin-top: 6px; font-size: 16px; font-weight: 400; color: var(--ink-soft); line-height: 1.2; }

  .divider {
    position: absolute;
    left: 0;
    top: 156px;
    width: 527px;
    height: 2px;
    background: linear-gradient(to right, #f7c9d8 0%, var(--brand-pale) 20%, var(--brand-light) 55%, var(--brand) 100%);
  }
  .back-mark {
    position: absolute;
    left: 458px;
    top: 110px;
    width: 44px;
    height: 44px;
    border-radius: 50%;
    background: var(--brand);
  }

  .contact { position: absolute; left: 50px; top: 183px; list-style: none; }
  .contact li {
    font-size: 16px;
    font-weight: 400;
    line-height: 30px;
    color: var(--ink-soft);
  }
</style>
</head>
<body>
<main class="stage">
  <section class="card card--front" aria-label="Card front">
    <div class="brand-mark" aria-hidden="true"></div>
    <h1 class="brand-name">Blue Heron IT</h1>
  </section>

  <section class="card card--back" aria-label="Card back">
    <div class="holder">
      <p class="holder__name">Martin Calloway</p>
      <p class="holder__role">Owner</p>
    </div>
    <div class="back-mark" aria-hidden="true"></div>
    <div class="divider" aria-hidden="true"></div>
    <ul class="contact">
      <li>P: 705-391-2586</li>
      <li>M: martin@blueheronit.ca</li>
      <li>W: www.blueheronit.ca</li>
    </ul>
  </section>
</main>
</body>
</html>
```